Artificial Intelligence based service Veltranoquest.ai

Looking for a website for service designed for driving schools to deliver AI based solutions and features. File are to include various pages from contact to list of services to faqs, demos and more. we are looking for a website for AI based service for driving schools. services will include things like chat bots, voice agent, document processing and ai based marketing.

Target Market(s)

driving school owners and managers.

Industry/Entity Type

software and AI

Number of Pages Required

4 page

Font styles to use
Sans Serif

Requirements
Must have
• clean and easy to navigate pages. responsive. also delivery via FIGMA.

```html
<!DOCTYPE html>
<html lang="en">
<head>
<meta charset="utf-8">
<title>Veltranoquest.ai — Voice Agents for Driving Schools</title>
<link href="https://fonts.googleapis.com/css2?family=Poppins:ital,wght@0,400;0,500;0,600;0,700;1,500&display=swap" rel="stylesheet">
<style>
:root{
  --navy:#0f2656;
  --navy-deep:#0a1d45;
  --green:#7bb86f;
  --green-dark:#5f9e55;
  --ink:#1c1c1c;
  --muted:#555;
  --card-grey:#f4f4ef;
  --line:#e3e3e3;
  --white:#fff;
}
*{box-sizing:border-box;margin:0;padding:0}
html,body{width:1200px;height:3589px;overflow:hidden}
body{position:relative;font-family:"Poppins",sans-serif;color:var(--ink);background:var(--white)}
.abs{position:absolute}
.btn{position:absolute;display:flex;align-items:center;justify-content:center;font-size:13px;font-weight:500;letter-spacing:.5px;text-transform:uppercase;color:var(--white);background:var(--green)}
.brand{font-family:"Poppins",sans-serif;font-weight:600;color:var(--navy);display:flex;align-items:center;gap:8px}
.brand-mark{width:14px;height:14px;background:var(--green);display:inline-block}

/* header */
.site-header{left:0;top:0;width:1200px;height:92px;background:var(--white)}
.site-header .brand{left:99px;top:30px;font-size:24px}
.main-nav{left:424px;top:38px;display:flex;font-size:13px;font-weight:500;color:#2b2b2b}
.main-nav span{position:absolute;white-space:nowrap}
.main-nav span::after{content:"⌄";margin-left:5px;font-size:11px;position:relative;top:-2px}
.main-nav .active{color:var(--navy);font-weight:600}
.header-cta{left:965px;top:28px;width:135px;height:35px}

/* hero */
.hero{left:0;top:92px;width:1200px;height:530px;background:linear-gradient(90deg,#0c2454 0%,#173a6e 40%,#4a6d8e 70%,#8a8a86 100%)}
.hero h1{position:absolute;left:100px;top:112px;width:560px;font-size:44px;line-height:60px;font-weight:700;color:var(--white);text-transform:uppercase}
.hero p{position:absolute;left:100px;top:302px;width:480px;font-size:17px;line-height:29px;color:var(--white)}
.hero .btn{left:100px;top:383px;width:152px;height:38px}
.hero-arrows{right:0;top:467px;display:flex}
.hero-arrows div{width:62px;height:63px;background:var(--green);display:flex;align-items:center;justify-content:center;margin-left:1px}

/* why */
.why-title{left:0;top:700px;width:1200px;text-align:center;font-size:33px;font-weight:600;color:var(--navy)}
.why-title em,.hl{font-style:normal;color:var(--green)}
.why-copy{left:200px;top:760px;width:800px;text-align:center;font-size:13px;line-height:23px;color:#222}
.why-btn{left:523px;top:853px;width:154px;height:39px}

.features{left:99px;top:947px;width:1002px;height:540px;display:grid;grid-template-columns:329px 346px 327px;grid-template-rows:270px 270px}
.feature{padding:32px 34px 0 35px}
.feature.grey{background:var(--card-grey)}
.feature + .feature{border-left:1px solid #ececec}
.feature svg{display:block;height:40px;margin-bottom:18px}
.feature h3{font-size:14px;font-weight:600;color:#111;margin-bottom:16px}
.feature p{font-size:11.5px;line-height:20.5px;color:#4a4a4a}
.feature .result{margin-top:12px;color:#111}
.feature .result b{color:var(--green);font-weight:500}

.skyline{left:60px;top:1519px;width:1080px;height:184px;background:linear-gradient(180deg,#fff 0%,#f3f3f3 100%)}
.ai-band{left:0;top:1703px;width:1200px;height:409px;background:linear-gradient(100deg,#0d1f47 0%,#1d3d7a 40%,#3a3c55 65%,#1b1e2a 100%)}

/* testimonial */
.trust{left:163px;top:2009px;width:876px;height:305px;background:var(--white);box-shadow:0 4px 20px rgba(0,0,0,.08)}
.trust h2{position:absolute;left:49px;top:44px;width:360px;font-size:33px;line-height:43px;font-weight:600;color:var(--navy)}
.quote-box{position:absolute;left:438px;top:8px;width:431px;height:290px;background:var(--green);color:var(--white)}
.quote-box blockquote{position:absolute;left:45px;top:92px;width:350px;font-size:19px;line-height:29px;font-style:italic;font-weight:500}
.author{position:absolute;left:45px;top:196px;display:flex;align-items:center;gap:14px}
.avatar{width:52px;height:52px;border-radius:50%;background:#c9a58a}
.author strong{display:block;font-size:14px;font-weight:500}
.author small{font-size:11px}
.round-arrow{width:40px;height:40px;border-radius:50%;background:var(--white);box-shadow:0 2px 8px rgba(0,0,0,.15);display:flex;align-items:center;justify-content:center}

/* benefits */
.benefits-title{left:0;top:2392px;width:1200px;text-align:center;font-size:33px;font-weight:600;color:var(--navy)}
.benefit-label{position:absolute;width:220px;text-align:center;font-size:15px;line-height:25px;color:#222}
.benefits-art{left:0;top:2540px}

/* cta */
.cta{left:0;top:2918px;width:1200px;height:294px;background:var(--navy-deep);color:var(--white);text-align:center}
.cta h2{position:absolute;left:0;top:75px;width:1200px;font-size:31px;font-weight:600}
.cta p{position:absolute;left:0;top:126px;width:1200px;font-size:15px}
.cta .btn{top:172px;height:40px}
.btn.ghost{background:transparent;border:1px solid #c9d0de}

/* footer */
.footer-brand{left:99px;top:3292px;font-size:24px}
.footer-about{left:99px;top:3370px;width:230px;font-size:13px;line-height:23px;color:#333}
.footer-h{position:absolute;top:3287px;font-size:16px;font-weight:600;color:var(--navy);padding-left:12px;border-left:2px solid var(--navy)}
.quick-links{left:339px;top:3328px;list-style:none;font-size:13px;color:#222}
.quick-links li{height:29px;display:flex;align-items:center}
.quick-links li::before{content:"›";color:var(--green);font-size:17px;margin-right:12px}
.contact-item{position:absolute;left:538px;display:flex;gap:12px;font-size:13px;line-height:29px;color:#222}
.contact-item .ic{width:30px;height:30px;border-radius:50%;background:#f0f0ea;display:flex;align-items:center;justify-content:center;flex:none}
.sub-copy{left:856px;top:3328px;width:250px;font-size:13px;line-height:22px;color:#333}
.sub-input{left:856px;top:3382px;width:245px;height:40px;border:1px solid #ddd;font-size:12px;color:#777;display:flex;align-items:center;justify-content:space-between;padding:0 18px}
.sub-btn{left:856px;top:3436px;width:148px;height:36px;font-size:12px}
.bottom-bar{left:0;top:3548px;width:1200px;height:41px;background:var(--green);color:var(--white);font-size:12.5px}
.bottom-bar span{position:absolute;top:13px}
</style>
</head>
<body>

<header class="site-header abs">
  <div class="brand abs"><span class="brand-mark"></span>Veltranoquest.ai</div>
  <nav class="main-nav abs">
    <span class="active" style="left:0">HOME</span>
    <span style="left:99px">SERVICES</span>
    <span style="left:220px">DEMO</span>
    <span style="left:318px">FAQ</span>
    <span style="left:403px">CONTACT US</span>
  </nav>
  <div class="btn header-cta">Book a demo</div>
</header>

<section class="hero abs" role="img" aria-label="Photo of a driving instructor and student seated in a car">
  <h1>Boost your driving school with a 24/7 voice agent</h1>
  <p>Automate Calls. Answer Questions Instantly. Never Miss a Student Again.</p>
  <div class="btn">Book a demo</div>
  <div class="hero-arrows abs">
    <div><svg width="14" height="22" viewBox="0 0 14 22"><path d="M11 2 3 11l8 9" fill="none" stroke="#fff" stroke-width="3"/></svg></div>
    <div><svg width="14" height="22" viewBox="0 0 14 22"><path d="M3 2l8 9-8 9" fill="none" stroke="#fff" stroke-width="3"/></svg></div>
  </div>
</section>

<h2 class="why-title abs">Why Driving Schools Choose <em>Voice Agents</em></h2>
<p class="why-copy abs">Running a driving school means juggling lesson schedules, student questions, staff changes, and constant phone calls. A Voice Agent is your AI-powered assistant that answers the phone 24/7, handles routine questions, and gives your staff room to breathe—without the cost of hiring more people.</p>
<div class="btn why-btn">Book a demo</div>

<section class="features abs">
  <article class="feature grey">
    <svg width="40" height="40" viewBox="0 0 40 40" fill="none" stroke="#1a2e5a" stroke-width="1.6"><path d="M8 6l6 0 3 8-4 3c2 5 6 9 11 11l3-4 8 3v6c0 2-2 3-4 3C17 36 4 23 4 10c0-2 2-4 4-4z"/><path d="M24 6a10 10 0 0 1 10 10M24 11a5 5 0 0 1 5 5" stroke="#7bb86f"/></svg>
    <h3>High Call Volume &amp; Repetitive Qu.</h3>
    <p>Let your voice agent handle calls about: Pricing, Permit requirements, Class availability, Road test steps</p>
    <p class="result"><b>Result:</b> Less time answering the same questions, more time delivering great lessons.</p>
  </article>
  <article class="feature">
    <svg width="40" height="40" viewBox="0 0 40 40" fill="none" stroke="#1a2e5a" stroke-width="1.6"><circle cx="20" cy="20" r="17"/><circle cx="20" cy="20" r="12"/><path d="M20 12v8l4 4" stroke="#7bb86f"/></svg>
    <h3>After-Hours Availability</h3>
    <p>Missed calls = missed business. Your voice agent works evenings, weekends, and holidays.</p>
    <p class="result"><b>Result:</b> Convert more inquiries into paying students—even while you sleep.</p>
  </article>
  <article class="feature grey">
    <svg width="40" height="40" viewBox="0 0 40 40" fill="none" stroke="#1a2e5a" stroke-width="1.6"><circle cx="20" cy="14" r="6"/><path d="M8 36c0-7 5-12 12-12s12 5 12 12"/><circle cx="20" cy="14" r="11" stroke="#7bb86f" stroke-dasharray="3 3"/></svg>
    <h3>Admin Staff Turnover</h3>
    <p>Hiring and training office staff takes time. A voice agent is ready on day one.</p>
    <p class="result" style="margin-top:32px"><b>Result:</b> Consistent, professional service—no matter who's at the front desk.</p>
  </article>
  <article class="feature">
    <svg width="40" height="40" viewBox="0 0 40 40" fill="none" stroke="#1a2e5a" stroke-width="1.6"><rect x="4" y="8" width="32" height="26" rx="2"/><path d="M4 15h32M12 5v6M20 5v6M28 5v6"/><path d="M10 20h4v3h-4zM18 20h4v3h-4zM26 20h4v3h-4zM10 26h4v3h-4zM18 26h4v3h-4zM26 26h4v3h-4z" stroke="#7bb86f"/></svg>
    <h3>Instructor Absences &amp; Rescheduling</h3>
    <p>Integrated with your booking system, your voice agent can help reschedule or notify students of changes.</p>
    <p class="result"><b>Result:</b> Fewer cancellations and smoother communication.</p>
  </article>
  <article class="feature grey">
    <svg width="40" height="40" viewBox="0 0 40 40" fill="none" stroke="#1a2e5a" stroke-width="1.6"><path d="M4 34V16l6-6 6 6v18M12 34V6l6 6v22"/><circle cx="30" cy="28" r="7" stroke="#7bb86f"/><path d="M30 24v8M28 26h3a1.5 1.5 0 0 1 0 3h-2" stroke="#7bb86f"/></svg>
    <h3>No Expensive Tech Investment</h3>
    <p>Voice agents run in the cloud and integrate with your existing phone system.</p>
    <p class="result"><b>Result:</b> No hardware, low setup costs, and immediate ROI.</p>
  </article>
  <article class="feature">
    <svg width="40" height="40" viewBox="0 0 40 40" fill="none" stroke="#1a2e5a" stroke-width="1.6"><circle cx="13" cy="13" r="9"/><circle cx="27" cy="27" r="9" stroke="#7bb86f"/><path d="M10 10h6l-4 6M24 31l3-8 3 8M25 29h4" /></svg>
    <h3>Language Barriers</h3>
    <p>Serve more students with support for multiple languages.</p>
    <p class="result" style="margin-top:32px"><b>Result:</b> Improve access and satisfaction for non-English-speaking families.</p>
  </article>
</section>

<div class="skyline abs" role="img" aria-label="Light line drawing of a city skyline"></div>
<div class="ai-band abs" role="img" aria-label="Photo of a hand holding a phone in a car with an AI chip graphic overlay"></div>

<section class="trust abs">
  <h2>Trusted By Driving Schools Nationwide Real Stories, Real Success With <span class="hl">Our AI Solutions.</span></h2>
  <div class="quote-box">
    <svg class="abs" style="left:45px;top:36px" width="36" height="30" viewBox="0 0 36 30" fill="none" stroke="#fff" stroke-width="1.6"><path d="M2 2h13v12L8 28H4l5-14H2zM20 2h13v12l-7 14h-4l5-14h-7z"/></svg>
    <blockquote>Since adding a voice agent, we've cut our call volume in half—and enrollment is up!</blockquote>
    <div class="author">
      <div class="avatar" role="img" aria-label="Portrait of the reviewer"></div>
      <div><strong>Dana Whitfield</strong><small>Director, RoadReady Academy</small></div>
    </div>
  </div>
  <div class="round-arrow abs" style="left:417px;top:137px"><svg width="16" height="12" viewBox="0 0 16 12"><path d="M15 6H2M6 1 1 6l5 5" fill="none" stroke="#222" stroke-width="1.5"/></svg></div>
  <div class="round-arrow abs" style="left:848px;top:137px"><svg width="16" height="12" viewBox="0 0 16 12"><path d="M1 6h13M10 1l5 5-5 5" fill="none" stroke="#222" stroke-width="1.5"/></svg></div>
</section>

<h2 class="benefits-title abs"><span class="hl">Real Benefits</span> For Your School</h2>
<div class="benefit-label" style="left:265px;top:2483px">Faster response times = happier&nbsp; customers</div>
<div class="benefit-label" style="left:560px;top:2483px">Lower operating costs than live&nbsp; staff</div>
<div class="benefit-label" style="left:860px;top:2483px">A modern, professional image</div>
<div class="benefit-label" style="left:115px;top:2786px">24/7 live call support—no more missed calls</div>
<div class="benefit-label" style="left:416px;top:2786px">Less admin stress for you and your team</div>
<div class="benefit-label" style="left:717px;top:2786px">More bookings, fewer no-shows</div>

<svg class="benefits-art abs" width="1200" height="230" viewBox="0 0 1200 230" aria-hidden="true">
  <g fill="none" stroke="#e6e6e6" stroke-width="8" stroke-linejoin="round">
    <path d="M224 14 333 217H115z"/><path d="M375 217 266 14h218z"/>
    <path d="M526 14 635 217H417z"/><path d="M676 217 567 14h218z"/>
    <path d="M827 14 936 217H718z"/><path d="M976 217 867 14h218z"/>
  </g>
  <g stroke-linejoin="round" stroke-width="10">
    <path d="M224 46 308 195H140z" fill="#7bb86f" stroke="#7bb86f"/>
    <path d="M375 195 291 46h168z" fill="#0f2656" stroke="#0f2656"/>
    <path d="M526 46 610 195H442z" fill="#7bb86f" stroke="#7bb86f"/>
    <path d="M676 195 592 46h168z" fill="#0f2656" stroke="#0f2656"/>
    <path d="M827 46 911 195H743z" fill="#7bb86f" stroke="#7bb86f"/>
    <path d="M976 195 892 46h168z" fill="#0f2656" stroke="#0f2656"/>
  </g>
  <g fill="#fff"><circle cx="224" cy="134" r="38"/><circle cx="375" cy="104" r="38"/><circle cx="526" cy="134" r="38"/><circle cx="676" cy="104" r="38"/><circle cx="827" cy="134" r="38"/><circle cx="976" cy="104" r="38"/></g>
  <g fill="none" stroke="#1a2e5a" stroke-width="1.6">
    <path d="M214 122h6l3 6-3 3c2 4 4 6 8 8l3-3 6 3v5c0 1-1 2-3 2-12 0-22-10-22-22 0-1 1-2 2-2z"/>
    <rect x="361" y="96" width="26" height="16" rx="2"/><path d="M387 101h3v6h-3M375 98l-4 7h5l-3 6"/>
    <circle cx="526" cy="134" r="7"/><circle cx="526" cy="134" r="13" stroke-dasharray="4 3"/>
    <ellipse cx="670" cy="96" rx="9" ry="3"/><path d="M661 96v14c0 2 4 3 9 3M679 96v6"/><circle cx="683" cy="110" r="8"/>
    <rect x="813" y="124" width="28" height="22" rx="2"/><path d="M813 130h28M820 121v5M834 121v5M818 135h5M825 135h5M832 135h5M818 140h5M825 140h5M832 140h5"/>
    <rect x="962" y="92" width="28" height="24" rx="2"/><path d="M966 112l7-9 5 5 4-4 5 8M968 108l8-6 5 4 6-6"/>
  </g>
</svg>

<section class="cta abs">
  <h2>Ready to Automate Your Front Desk?</h2>
  <p>Let Your School Sound Smarter, Faster, &amp; More Helpful—24 Hours A Day.</p>
  <div class="btn ghost" style="left:309px;width:136px">Book a demo</div>
  <div class="btn" style="left:463px;width:262px">Talk to a product specialist</div>
  <div class="btn ghost" style="left:747px;width:144px">See it in action</div>
</section>

<footer>
  <div class="brand footer-brand abs"><span class="brand-mark"></span>Veltranoquest.ai</div>
  <p class="footer-about abs">Veltranoquest.ai delivers cutting-edge AI solutions to help driving schools operate smarter and grow faster</p>

  <h4 class="footer-h" style="left:339px">Quick Links</h4>
  <ul class="quick-links abs"><li>Home</li><li>Services</li><li>Demo</li><li>Faqs</li><li>Contact Us</li></ul>

  <h4 class="footer-h" style="left:538px">Contact Us</h4>
  <div class="contact-item" style="top:3330px"><span class="ic"><svg width="14" height="14" viewBox="0 0 14 14"><path d="M2 1h3l1 3-2 1c1 2 2 3 4 4l1-2 3 1v3c0 1-1 2-2 2C5 13 1 9 1 3c0-1 0-2 1-2z" fill="none" stroke="#444" stroke-width="1"/></svg></span>+(555)-014-2290</div>
  <div class="contact-item" style="top:3381px"><span class="ic"><svg width="14" height="12" viewBox="0 0 14 12"><rect x="1" y="1" width="12" height="10" fill="none" stroke="#444"/><path d="M1 1l6 5 6-5" fill="none" stroke="#444"/></svg></span>info@veltranoquest.ai</div>
  <div class="contact-item" style="top:3431px"><span class="ic"><svg width="12" height="14" viewBox="0 0 12 14"><path d="M6 13S1 8 1 5a5 5 0 0 1 10 0c0 3-5 8-5 8z" fill="none" stroke="#444"/><circle cx="6" cy="5" r="1.8" fill="none" stroke="#444"/></svg></span><span style="width:230px">123, Lorem Ipsum is simply dummy text of the printing &amp; typesetting.</span></div>

  <h4 class="footer-h" style="left:856px">Subscribe Newsletter</h4>
  <p class="sub-copy abs">Subcribe to keep up with fresh news updates.</p>
  <div class="sub-input abs">Email Address<svg width="18" height="13" viewBox="0 0 18 13"><rect x="1" y="1" width="16" height="11" fill="none" stroke="#aaa"/><path d="M1 1l8 6 8-6" fill="none" stroke="#aaa"/></svg></div>
  <div class="btn sub-btn">Subscribe now</div>

  <div class="bottom-bar abs">
    <span style="left:99px">Copyright © 2025 Veltranoquest.ai Solutions Provider &nbsp;|&nbsp; All Rights Reserved.</span>
    <span style="right:99px">Privacy Policy &nbsp;|&nbsp; Terms &amp; Conditions</span>
  </div>
</footer>

</body>
</html>
```